Business Card Design Project

We need a business card design for a relatively new company called Velmar Gear. We design paddle (an outdoor winter sport primarily played in the midwest and east coast) and tennis bags for women and men. Velmar Gear is a lifestyle brand for the next generation country club goers. Our bags merge fashion with functionality and are making country club sports trendier and more fashionable.

I would like to include space for
Name: (will fill this in for employees)
Velmar Gear
Phone: (will do this)
Email:
www.velmargear.example

Would also like to include Chatterbook and Flitter icons.
Please do not use pictures of the bags - this is just to give you an idea of what style bags we sell.

Target Market(s)

30 to 40 year old men and women - luxury market

Industry/Entity Type

Fashion

Requirements
Must have
• Would like the company logo included

```html
<!DOCTYPE html>
<html lang="en">
<head>
<meta charset="utf-8">
<title>Velmar Gear — Business Card</title>
<link rel="stylesheet" href="https://fonts.googleapis.com/css2?family=Questrial&family=Parisienne&display=swap">
<style>
  :root {
    --slate-dark: #354246;
    --slate-mid: #5a686b;
    --slate-glow: #7b8789;
    --tab-light: #eeeef2;
    --tab-dark: #4b5a5b;
    --paper-light: #f4f4f6;
    --paper-mid: #c9d0d2;
    --paper-edge: #bcc4c6;
    --ink: #4f5c5e;
    --white: #f3f3f5;
    --flitter: #5fe0d6;
    --chatter: #3b5db4;
  }
  * { margin: 0; padding: 0; box-sizing: border-box; }
  html, body { width: 1042px; height: 1200px; overflow: hidden; }
  body { position: relative; background: var(--paper-mid); }

  .card-front {
    position: absolute; left: 0; top: 0; width: 1042px; height: 600px;
    background: radial-gradient(ellipse 420px 360px at 521px 270px, var(--slate-glow) 0%, var(--slate-mid) 45%, var(--slate-dark) 100%);
  }
  .card-back {
    position: absolute; left: 0; top: 600px; width: 1042px; height: 600px;
    background: radial-gradient(ellipse 520px 380px at 560px 280px, var(--paper-light) 0%, #dde1e3 45%, var(--paper-edge) 100%);
  }
  .side-tab {
    position: absolute; width: 28px; height: 367px;
  }
  .side-tab--left { left: 0; border-radius: 0 18px 18px 0 / 0 60px 60px 0; }
  .side-tab--right { right: 0; border-radius: 18px 0 0 18px / 60px 0 0 60px; }
  .card-front .side-tab { top: 117px; background: var(--tab-light); }
  .card-back .side-tab { top: 115px; background: var(--tab-dark); }

  .brand {
    position: absolute; left: 195px; top: 222px;
    display: flex; align-items: center; gap: 30px;
  }
  .brand-mark {
    width: 120px; height: 120px; border-radius: 50%;
    border: 0; background: var(--white);
  }
  .brand-name {
    font-family: "Questrial", sans-serif; font-size: 96px; line-height: 1;
    color: var(--white); letter-spacing: 1px;
  }
  .web-address {
    position: absolute; left: 0; right: 0; top: 558px; text-align: center;
    font-family: "Parisienne", cursive; font-size: 32px; color: var(--white);
  }

  .pattern-field { position: absolute; inset: 0; background: linear-gradient(180deg, rgba(180,190,192,0.25), rgba(255,255,255,0) 40%, rgba(180,190,192,0.2)); }

  .contact {
    position: absolute; left: 82px; top: 230px; list-style: none;
    font-family: "Parisienne", cursive; font-size: 29px; line-height: 36.5px; color: var(--ink);
  }
  .social {
    position: absolute; right: 20px; bottom: 14px; display: flex; gap: 16px; align-items: center;
  }
  .social-item {
    display: flex; align-items: center; gap: 6px;
    font-family: "Questrial", sans-serif; font-size: 15px; color: var(--ink);
  }
  .social-dot { width: 22px; height: 22px; border-radius: 4px; }
  .social-dot--flitter { background: var(--flitter); }
  .social-dot--chatter { background: var(--chatter); }
</style>
</head>
<body>
  <section class="card-front">
    <div class="side-tab side-tab--left"></div>
    <div class="side-tab side-tab--right"></div>
    <div class="brand">
      <div class="brand-mark"></div>
      <div class="brand-name">Velmar Gear</div>
    </div>
    <div class="web-address">www.velmargear.example</div>
  </section>

  <section class="card-back">
    <div class="pattern-field" role="img" aria-label="Faint repeating brand-mark pattern on light silver linen"></div>
    <div class="side-tab side-tab--left"></div>
    <div class="side-tab side-tab--right"></div>
    <ul class="contact">
      <li>Name : (will fill this in for employees)</li>
      <li>Velmar Gear</li>
      <li>Phone : (will do this)</li>
      <li>Email :</li>
    </ul>
    <div class="social">
      <span class="social-item"><span class="social-dot social-dot--flitter"></span>Flitter</span>
      <span class="social-item"><span class="social-dot social-dot--chatter"></span>Chatterbook</span>
    </div>
  </section>
</body>
</html>
```